Company growth chart/Vision for the next 10 years of growth

I need to show an illustration how the company will grow over the next 10 years. Develop graphic to communicate:

In the center / or main focus ar...

Target Market(s)

Employees in corporate / need to show a future vision to get everyone excited about. Not a growth "tree".

Industry/Entity Type

It Company

Requirements
Must have
• Be an illustration/graphic showing what the project description states.
Nice to have
• I've looked at gears/mountains/icons to showcase this vision and I haven't been able to come up with anything.
Should not have
• A growth tree. Not what I'm looking for. This is corporate.

```html
<!DOCTYPE html>
<html lang="en">
<head>
<meta charset="utf-8">
<title>Vision 2026</title>
<link rel="stylesheet" href="https://fonts.googleapis.com/css2?family=Open+Sans:wght@400;700&family=Merriweather:wght@700;900&display=swap">
<style>
  :root {
    --bg-light: #93b9e0;
    --bg-mid: #74a3d3;
    --bg-dark: #5f90c6;
    --gear-light: #f1f1f1;
    --gear-mid: #c9cbce;
    --gear-dark: #9a9da2;
    --disc-light: #3d86d0;
    --disc-dark: #1e5aa8;
    --accent-yellow: #f4d21c;
    --label-white: #ffffff;
    --vision-blue: #2c66b0;
    --bar-orange: #f05a1a;
    --bar-gold: #f5b400;
    --bar-amber: #f39c12;
    --bar-lime: #b7c925;
    --icon-teal: #1a9c92;
    --icon-orange: #f2993a;
  }
  html, body {
    margin: 0;
    padding: 0;
    width: 1200px;
    height: 894px;
    overflow: hidden;
    background: var(--bg-mid);
  }
  .vision-board {
    display: block;
    width: 1200px;
    height: 894px;
    font-family: "Open Sans", Arial, sans-serif;
  }
  .label-heading {
    fill: var(--accent-yellow);
    font-weight: 700;
    font-size: 12.5px;
    letter-spacing: -0.2px;
  }
  .label-item {
    fill: var(--label-white);
    font-size: 12.5px;
  }
  .connector {
    fill: none;
    stroke: var(--label-white);
    stroke-width: 2;
  }
  .connector-dot { fill: var(--label-white); }
  .bullet { fill: none; stroke: var(--label-white); stroke-width: 1.3; }
  .bullet-core { fill: var(--label-white); }
  .vision-word {
    font-family: "Merriweather", Georgia, serif;
    font-weight: 900;
    font-size: 34px;
    fill: #ffffff;
    stroke: var(--vision-blue);
    stroke-width: 1.2;
    letter-spacing: 2px;
  }
  .vision-year {
    font-family: "Merriweather", Georgia, serif;
    font-weight: 700;
    font-size: 64px;
    fill: var(--vision-blue);
  }
  .gear-teeth { fill: none; stroke: url(#gearMetal); stroke-width: 16; stroke-dasharray: 14.4 14.5; }
  .gear-body { fill: url(#gearMetal); }
  .gear-rim { fill: var(--gear-light); stroke: var(--gear-dark); stroke-width: 1; }
  .gear-disc { fill: url(#discBlue); }
  .faint-gear { fill: #ffffff; opacity: 0.06; }
</style>
</head>
<body>
<svg class="vision-board" viewBox="0 0 1200 894" xmlns="http://www.w3.org/2000/svg">
  <defs>
    <radialGradient id="boardBg" cx="50%" cy="45%" r="75%">
      <stop offset="0" stop-color="var(--bg-light)"/>
      <stop offset="0.6" stop-color="var(--bg-mid)"/>
      <stop offset="1" stop-color="var(--bg-dark)"/>
    </radialGradient>
    <linearGradient id="gearMetal" x1="0" y1="0" x2="1" y2="1">
      <stop offset="0" stop-color="var(--gear-light)"/>
      <stop offset="0.55" stop-color="var(--gear-mid)"/>
      <stop offset="1" stop-color="var(--gear-dark)"/>
    </linearGradient>
    <linearGradient id="discBlue" x1="0" y1="0" x2="1" y2="1">
      <stop offset="0" stop-color="var(--disc-light)"/>
      <stop offset="1" stop-color="var(--disc-dark)"/>
    </linearGradient>
    <linearGradient id="sceneFill" x1="0" y1="0" x2="0" y2="1">
      <stop offset="0" stop-color="#8fd6d8"/>
      <stop offset="0.45" stop-color="#bfe6e4"/>
      <stop offset="0.62" stop-color="#9a6a3f"/>
      <stop offset="0.85" stop-color="#5a3a1c"/>
      <stop offset="1" stop-color="#3f9b3a"/>
    </linearGradient>
    <linearGradient id="mapFill" x1="0" y1="0" x2="1" y2="1">
      <stop offset="0" stop-color="#d9d27a"/>
      <stop offset="0.5" stop-color="#c99a4c"/>
      <stop offset="1" stop-color="#5f9e4a"/>
    </linearGradient>
    <g id="gear">
      <circle class="gear-teeth" r="92"/>
      <circle class="gear-body" r="86"/>
      <circle class="gear-rim" r="78"/>
    </g>
    <path id="visionArc" d="M -110 0 A 115 115 0 0 1 110 0"/>
  </defs>

  <!-- Backdrop -->
  <rect class="backdrop" width="1200" height="894" fill="url(#boardBg)"/>
  <g class="backdrop-gears">
    <circle class="faint-gear" cx="230" cy="170" r="150"/>
    <circle class="faint-gear" cx="1080" cy="140" r="120"/>
    <circle class="faint-gear" cx="1120" cy="720" r="90"/>
    <circle class="faint-gear" cx="650" cy="170" r="110"/>
    <circle class="faint-gear" cx="760" cy="840" r="130"/>
  </g>

  <!-- Centre gear: Vision 2026 -->
  <g class="gear-hub gear-vision" transform="translate(587 438)">
    <use href="#gear" transform="scale(1.95)"/>
    <circle r="142" fill="url(#sceneFill)" role="img" aria-label="Mountain landscape with pine trees under a clear sky"/>
    <g transform="translate(0 -40)">
      <text class="vision-word" text-anchor="middle"><textPath href="#visionArc" startOffset="50%">VISION</textPath></text>
    </g>
    <text class="vision-year" x="0" y="-10" text-anchor="middle">2026</text>
  </g>

  <!-- Develop our people -->
  <g class="gear-hub gear-people" transform="translate(367 209)">
    <use href="#gear" transform="scale(1.12)"/>
    <circle class="gear-disc" r="80"/>
    <g class="growth-bars">
      <rect x="-45" y="32" width="15" height="22" fill="var(--bar-orange)"/>
      <rect x="-25" y="10" width="17" height="44" fill="var(--bar-gold)"/>
      <rect x="-3" y="-2" width="17" height="56" fill="var(--bar-amber)"/>
      <rect x="19" y="0" width="17" height="54" fill="var(--bar-lime)"/>
      <path d="M -58 36 L 2 -10" stroke="#fff" stroke-width="4" fill="none"/>
      <path d="M 8 -14 L -8 -12 L 0 0 Z" fill="#fff"/>
    </g>
    <circle cx="22" cy="-30" r="16" fill="#2a4b7c" opacity="0.5" role="img" aria-label="Cheering businessman standing on the tallest bar"/>
  </g>

  <!-- Grow our team -->
  <g class="gear-hub gear-team" transform="translate(855 235)">
    <use href="#gear" transform="scale(1.12)"/>
    <circle class="gear-disc" r="80"/>
    <ellipse cx="-50" cy="-2" rx="15" ry="20" fill="#e8eef6" opacity="0.85" role="img" aria-label="Small group of people"/>
    <ellipse cx="18" cy="14" rx="46" ry="48" fill="var(--accent-yellow)" opacity="0.9" role="img" aria-label="Large crowd of people"/>
    <path d="M -48 -38 Q -20 -62 12 -46" stroke="#fff" stroke-width="5" fill="none"/>
    <path d="M 20 -42 L 6 -56 L 4 -40 Z" fill="#fff"/>
  </g>

  <!-- Be the best -->
  <g class="gear-hub gear-best" transform="translate(898 530)">
    <use href="#gear"/>
    <circle class="gear-disc" r="73"/>
    <path d="M -48 -20 L -30 -40 L 30 -40 L 48 -20 L 0 40 Z" fill="var(--accent-yellow)" stroke="#1f4f9a" stroke-width="3" role="img" aria-label="Excellence badge with stars"/>
  </g>

  <!-- Vertical markets -->
  <g class="gear-hub gear-markets" transform="translate(311 551)">
    <use href="#gear" transform="scale(1.17)"/>
    <circle class="gear-disc" r="84"/>
    <g class="market-icons">
      <rect x="-52" y="-22" width="36" height="26" fill="var(--icon-orange)"/>
      <rect x="-40" y="-10" width="12" height="14" fill="var(--disc-dark)"/>
      <rect x="-56" y="-32" width="44" height="10" fill="var(--icon-orange)"/>
      <rect x="2" y="-56" width="28" height="60" fill="var(--accent-yellow)"/>
      <rect x="30" y="-30" width="10" height="34" fill="var(--accent-yellow)"/>
      <circle cx="-32" cy="32" r="20" fill="#f6e7b0" stroke="var(--accent-yellow)" stroke-width="3" role="img" aria-label="Trade worker icon"/>
      <rect x="-2" y="14" width="44" height="38" fill="var(--icon-teal)"/>
      <rect x="-8" y="10" width="56" height="6" fill="var(--icon-teal)"/>
    </g>
  </g>

  <!-- Regional market -->
  <g class="gear-hub gear-regional" transform="translate(714 724)">
    <use href="#gear" transform="scale(1.17)"/>
    <circle class="gear-disc" r="84"/>
    <g class="regional-icons" fill="var(--accent-yellow)">
      <path d="M -60 22 L -38 2 L -16 22 L -20 22 L -20 52 L -56 52 L -56 22 Z"/>
      <rect x="-44" y="36" width="10" height="16" fill="var(--disc-dark)"/>
      <rect x="-10" y="-40" width="46" height="92"/>
      <rect x="36" y="-18" width="14" height="70"/>
      <g fill="var(--disc-dark)">
        <rect x="-4" y="-30" width="34" height="4"/>
        <rect x="-4" y="-18" width="34" height="4"/>
        <rect x="-4" y="-6" width="34" height="4"/>
        <rect x="-4" y="6" width="34" height="4"/>
        <rect x="-4" y="18" width="34" height="4"/>
        <rect x="-4" y="30" width="34" height="4"/>
      </g>
    </g>
  </g>

  <!-- Label: develop our people -->
  <g class="callout">
    <text class="label-heading" x="98" y="166">How? Develop Our People</text>
    <circle class="connector-dot" cx="163" cy="186" r="5"/>
    <polyline class="connector" points="163,186 190,219 256,219"/>
  </g>

  <!-- Label: grow our team -->
  <g class="callout">
    <text class="label-heading" x="969" y="140">How? Grow Our Team</text>
    <circle class="connector-dot" cx="1051" cy="158" r="5"/>
    <polyline class="connector" points="1051,158 1008,178 954,178"/>
  </g>

  <!-- Label: be the best -->
  <g class="callout">
    <text class="label-heading" x="1010" y="420">How? Be The Best</text>
    <circle class="connector-dot" cx="1024" cy="434" r="5"/>
    <polyline class="connector" points="1024,434 1003,462 972,462"/>
  </g>

  <!-- Label: vertical markets -->
  <g class="callout">
    <text class="label-heading" x="41" y="309">How? Embrace Vertical Market Focus</text>
    <g class="market-list">
      <rect x="62" y="326" width="13" height="24" fill="var(--accent-yellow)"/>
      <circle cx="94" cy="342" r="4" class="bullet"/><circle cx="94" cy="342" r="1.5" class="bullet-core"/>
      <text class="label-item" x="107" y="346">Hotels</text>

      <circle cx="69" cy="374" r="11" fill="#f6e7b0" stroke="var(--accent-yellow)" stroke-width="2"/>
      <circle cx="94" cy="375" r="4" class="bullet"/><circle cx="94" cy="375" r="1.5" class="bullet-core"/>
      <text class="label-item" x="107" y="379">Trade Labor Subcontracting</text>

      <rect x="59" y="404" width="20" height="13" fill="var(--icon-orange)"/>
      <circle cx="94" cy="410" r="4" class="bullet"/><circle cx="94" cy="410" r="1.5" class="bullet-core"/>
      <text class="label-item" x="107" y="414">Specialty Retail</text>

      <rect x="60" y="436" width="20" height="16" fill="var(--icon-teal)"/>
      <circle cx="94" cy="444" r="4" class="bullet"/><circle cx="94" cy="444" r="1.5" class="bullet-core"/>
      <text class="label-item" x="107" y="448">Quick Service Restaurants</text>
    </g>
    <circle class="connector-dot" cx="166" cy="469" r="5"/>
    <polyline class="connector" points="166,469 166,520 204,556"/>
  </g>

  <!-- Regional map -->
  <rect class="region-map" x="122" y="688" width="179" height="128" fill="url(#mapFill)" role="img" aria-label="Regional map of the upper Midwest with service locations marked"/>

  <!-- Label: regional market -->
  <g class="callout">
    <text class="label-heading" x="336" y="724">How? Continue Regional Market Focus</text>
    <circle cx="370" cy="741" r="4" class="bullet"/><circle cx="370" cy="741" r="1.5" class="bullet-core"/>
    <text class="label-item" x="383" y="745">Commercial</text>
    <circle cx="370" cy="764" r="4" class="bullet"/><circle cx="370" cy="764" r="1.5" class="bullet-core"/>
    <text class="label-item" x="383" y="768">Residential</text>
    <circle class="connector-dot" cx="507" cy="732" r="5"/>
    <polyline class="connector" points="507,732 524,753 600,753"/>
  </g>

  <!-- Why -->
  <g class="callout why">
    <text class="label-heading" x="954" y="655">Why?</text>
    <circle cx="953" cy="677" r="3.5" class="bullet"/><circle cx="953" cy="677" r="1.3" class="bullet-core"/>
    <text class="label-item" x="961" y="681">To enrich the lives of those</text>
    <text class="label-item" x="966" y="697">we serve</text>
    <circle cx="953" cy="710" r="3.5" class="bullet"/><circle cx="953" cy="710" r="1.3" class="bullet-core"/>
    <text class="label-item" x="961" y="714">Provide our customers with a</text>
    <text class="label-item" x="966" y="730">more enjoyable building experience</text>
    <circle cx="953" cy="742" r="3.5" class="bullet"/><circle cx="953" cy="742" r="1.3" class="bullet-core"/>
    <text class="label-item" x="961" y="746">Provide fulfilling careers for our</text>
    <text class="label-item" x="961" y="762">people filled with opportunity</text>
  </g>
</svg>
</body>
</html>
```